Upmarket building and construction company needs signage

Our building company R Brent Construction, needs signage to put up on the side of our vehicle trailers and on site fencing. We are a building company that specialises in residential construction and carpentry .

I will attach our logo and some inspirational pics for site fencing as well as what our trailer looks like .
Other details i would like on the sign are our
( email) rbrentconstruction@mailbox-example.net
(mobile ) 0493 518 264
(website ) rbrentconstruction. example.net

Target Market(s)

Home owners looking for a reliable local builder who produces good quality work. I have attached some inspirational pics.

Industry/Entity Type

Building and Construction

Colors

Designer to choose colors to be used in the design.

Requirements
Must have
• Our logo, contact information
Nice to have
• We would like the design to have elements of being Elegant, Serious, Modern, Professional, Masculine, Conservative and Upmarket.

```html
<!DOCTYPE html>
<html lang="en">
<head>
<meta charset="UTF-8">
<title>R Brent Construction — Site Fence Banner</title>
<link rel="stylesheet" href="https://fonts.googleapis.com/css2?family=Jost:wght@300;400&display=swap">
<style>
  :root {
    --backdrop: #c9c9c9;
    --panel-dark: #000000;
    --panel-light: #ffffff;
    --ink-light: #ffffff;
    --ink-grey: #555555;
    --shade-dark-a: #262626;
    --shade-dark-b: #101010;
    --shade-light-a: #e6e6e6;
    --shade-light-b: #f6f6f6;
    --shadow: rgba(0, 0, 0, 0.28);
  }
  * { margin: 0; padding: 0; box-sizing: border-box; }
  html, body {
    width: 1056px;
    height: 1200px;
    overflow: hidden;
    background: var(--backdrop);
    font-family: "Jost", "Futura", sans-serif;
  }
  .canvas {
    position: relative;
    width: 1056px;
    height: 1200px;
  }
  .banner {
    position: absolute;
    left: 38px;
    top: 417px;
    width: 980px;
    height: 366px;
    display: flex;
    box-shadow: 8px 10px 10px var(--shadow);
  }
  .banner__brand {
    width: 609px;
    height: 100%;
    background: var(--panel-dark);
    position: relative;
    overflow: hidden;
  }
  .brand-backdrop {
    position: absolute;
    left: 40px;
    top: 82px;
    width: 160px;
    height: 274px;
    background: linear-gradient(180deg, var(--shade-dark-a), var(--shade-dark-b));
  }
  .brand-mark-area {
    position: absolute;
    left: 380px;
    top: 30px;
    width: 188px;
    height: 136px;
    background: linear-gradient(180deg, var(--shade-dark-a), var(--shade-dark-b));
  }
  .brand-block {
    position: absolute;
    right: 41px;
    bottom: 28px;
    text-align: left;
    color: var(--ink-light);
  }
  .brand-name {
    font-weight: 300;
    color: var(--ink-light);
    line-height: 1;
  }
  .brand-name__main {
    display: block;
    font-size: 86px;
    letter-spacing: 2px;
    margin-bottom: 12px;
  }
  .brand-name__sub {
    display: block;
    font-size: 42px;
    letter-spacing: 3px;
  }
  .brand-tagline {
    margin-top: 8px;
    font-weight: 400;
    font-size: 22px;
    letter-spacing: 2.8px;
    color: var(--ink-light);
  }
  .banner__contact {
    flex: 1;
    height: 100%;
    background: var(--panel-light);
    position: relative;
    padding: 30px 0 0 33px;
    color: var(--ink-grey);
  }
  .contact-backdrop {
    position: absolute;
    left: 33px;
    top: 135px;
    width: 305px;
    height: 231px;
    background: linear-gradient(180deg, var(--shade-light-a), var(--shade-light-b));
  }
  .contact-phone {
    position: relative;
    font-weight: 400;
    font-size: 48px;
    line-height: 1;
    letter-spacing: 0.5px;
  }
  .contact-email {
    position: relative;
    margin-top: 6px;
    font-size: 17px;
    letter-spacing: -0.1px;
  }
  .contact-web {
    position: absolute;
    left: 33px;
    bottom: 26px;
    font-size: 22px;
    letter-spacing: -0.2px;
    background: var(--panel-light);
    padding-right: 4px;
  }
</style>
</head>
<body>
  <main class="canvas">
    <section class="banner" aria-label="Site fence banner">
      <div class="banner__brand">
        <div class="brand-backdrop" role="img" aria-label="Faint large brand symbol decoration"></div>
        <div class="brand-mark-area" role="img" aria-label="Company brand symbol"></div>
        <div class="brand-block">
          <h1 class="brand-name">
            <span class="brand-name__main">R BRENT</span>
            <span class="brand-name__sub">CONSTRUCTION</span>
          </h1>
          <p class="brand-tagline">BUILDING AND CARPENTRY</p>
        </div>
      </div>
      <div class="banner__contact">
        <div class="contact-backdrop" role="img" aria-label="Grey brand symbol decoration"></div>
        <p class="contact-phone">0493 518 264</p>
        <p class="contact-email">rbrentconstruction@mailbox-example.net</p>
        <p class="contact-web">rbrentconstruction.example.net</p>
      </div>
    </section>
  </main>
</body>
</html>
```